MOREVI VEGAN SUSHI

www.morevi-restaurant.de
We are open in 2018 and are an innovative restaurant from Munich. We would like a cool design for our drinks and food menu. It's very simple at the moment. See the File menu. In any case, our logo should appear. On the website we use neutraface as a font. But it's not a must. We are only open in the evening and appeal to a young, upscale audience.

```html
<!DOCTYPE html>
<html lang="de">
<head>
<meta charset="utf-8">
<title>Morevi – Karte</title>
<link rel="stylesheet" href="https://fonts.googleapis.com/css2?family=Josefin+Sans:wght@300;400&family=Oswald:wght@300&family=Roboto:wght@300;400&family=Roboto+Condensed:wght@300&display=swap">
<style>
  :root {
    --page: #ffffff;
    --ink: #231f20;
    --black: #000000;
    --paper: #f1ead9;
    --price: #e35a6e;
    --vegan: #1f9a3d;
    --white: #ffffff;
    --sketch: #d8d0bd;
  }
  * { margin: 0; padding: 0; box-sizing: border-box; }
  html, body { width: 1149px; height: 1200px; overflow: hidden; background: var(--page); }
  body { position: relative; font-family: "Roboto", Arial, sans-serif; color: var(--ink); }

  .cover {
    position: absolute; left: 252px; top: 148px; width: 547px; height: 385px;
    background: radial-gradient(ellipse at 50% 100%, #2a2a2a 0%, #0c0c0c 45%, #000 75%);
    color: var(--white);
  }
  .cover__name {
    position: absolute; left: 0; right: 0; top: 118px; text-align: center;
    font-family: "Josefin Sans", sans-serif; font-weight: 300; font-size: 34px; letter-spacing: 10px;
  }
  .cover__sub {
    position: absolute; left: 0; right: 0; top: 192px; text-align: center;
    font-family: "Josefin Sans", sans-serif; font-weight: 300; font-size: 11px; letter-spacing: 8px;
  }
  .cover__web {
    position: absolute; left: 0; right: 0; top: 235px; text-align: center;
    font-size: 6px; letter-spacing: 0.2px;
  }
  .cover__contacts {
    position: absolute; left: 27px; right: 27px; top: 365px;
    display: flex; justify-content: space-between;
    font-weight: 300; font-size: 9px; letter-spacing: 0.1px;
  }

  .menu-card {
    position: absolute; left: 376px; top: 557px; width: 546px; height: 386px;
    background: radial-gradient(ellipse at 50% 100%, #2a2a2a 0%, #0c0c0c 45%, #000 75%);
  }
  .menu {
    position: absolute; left: 25px; top: 26px; width: 496px; height: 334px;
    background: var(--paper);
  }
  .menu__title {
    position: absolute; left: 0; right: 0; top: 6px; text-align: center;
    font-family: "Oswald", sans-serif; font-weight: 300; font-size: 41px; line-height: 1; letter-spacing: -1px;
  }
  .section { position: absolute; width: 118px; font-weight: 300; font-size: 7.4px; line-height: 9.3px; }
  .section__head {
    background: var(--black); color: var(--white); text-align: center;
    height: 10px; line-height: 10px; font-size: 7.4px; margin-bottom: 3px;
  }
  .row { display: flex; justify-content: space-between; }
  .price { color: var(--price); white-space: nowrap; }
  .condensed { font-family: "Roboto Condensed", sans-serif; font-size: 6.8px; }
  .condensed .row { height: 14px; line-height: 10px; }
  .spaced { line-height: 11px; }
  .dessert .row { height: 11px; }
  .dessert .section__head { font-family: "Roboto", sans-serif; font-size: 7.4px; }
  .vegan {
    position: absolute; left: 374px; width: 118px; top: 263px; text-align: center;
    color: var(--vegan); font-size: 9px;
  }
  .allergy {
    position: absolute; left: 374px; width: 118px; top: 279px; text-align: center;
    font-size: 9px; line-height: 10.3px;
  }
  .sketch { position: absolute; background: var(--sketch); border-radius: 6px; opacity: 0.7; }
</style>
</head>
<body>

<section class="cover">
  <div class="cover__name">MOREVI</div>
  <div class="cover__sub">VEGAN SUSHI</div>
  <div class="cover__web">WWW.MOREVI-RESTAURANT.DE</div>
  <div class="cover__contacts">
    <span>089 | 555012340</span>
    <span>LINDENSTRASSE 14</span>
    <span>80799 MÜNCHEN</span>
    <span>WELCOME@MOREVI-RESTAURANT.DE</span>
  </div>
</section>

<section class="menu-card">
  <div class="menu">
    <h1 class="menu__title">MENU</h1>

    <div class="section" style="left:5px; top:61px;">
      <div class="section__head">CHEF MEN mit Aperitiv</div>
      <div>für 2 Personen</div>
      <div>KleinePortion RAMENSUPPE</div>
      <div>mit Gemüse &amp; Nudeln</div>
      <div>MINI SET</div>
      <div class="row"><span>DESSERT</span><span class="price">81,00€</span></div>
    </div>

    <div class="section" style="left:5px; top:128px;">
      <div class="section__head">OMAKASE</div>
      <div>für 2 Personen</div>
      <div>EDAMAME OMAKASE SET mit 8</div>
      <div>Spezialitäten des Hauses</div>
      <div class="row"><span>PANA COTTAmitBeeren</span><span class="price">68,00€</span></div>
    </div>

    <div class="sketch" role="img" aria-label="Linienzeichnung zweier Sushi-Rollen" style="left:34px; top:188px; width:59px; height:35px;"></div>

    <div class="section" style="left:5px; top:234px;">
      <div class="section__head">SET 1</div>
      <div>HOSOMAKI</div>
      <div>FUTOMAKI</div>
      <div>NIGIRI</div>
      <div>KÜRBISKROKETTEN</div>
      <div>WAKAME GURKEN SALAT</div>
      <div>PICKLES</div>
      <div>GYOZA TEIGTASCHEN</div>
      <div class="row"><span>SUSHI CAKE</span><span class="price">33,90€</span></div>
    </div>

    <div class="section" style="left:127px; top:61px;">
      <div class="section__head">SET 2</div>
      <div>HOSOMAKI</div>
      <div>FUTOMAKI</div>
      <div>PICKLES</div>
      <div>SUSHI "THUNA" CAKE</div>
      <div>Crispy AUBERGINEN mit Mayo</div>
      <div class="row"><span>AUBERGINE DENGAKU</span><span class="price">31,90€</span></div>
    </div>

    <div class="section" style="left:127px; top:136px;">
      <div class="section__head">SET 3</div>
      <div>HOSOMAKI</div>
      <div>URAMAKI</div>
      <div>NIGIRI</div>
      <div>GEMÜSE TEMPURA</div>
      <div>Crispy TOFUSTICKS mit Mayo</div>
      <div class="row"><span>WAKAME SHIRA AE</span><span class="price">28,90€</span></div>
    </div>

    <div class="sketch" role="img" aria-label="Linienzeichnung von Stäbchen mit Sushi-Rolle und Sojasaucenflasche" style="left:128px; top:210px; width:100px; height:114px;"></div>

    <div class="section" style="left:251px; top:61px;">
      <div class="section__head">VORSPEISEN</div>
      <div class="row"><span>MISO SUPPE</span><span class="price">5,50€</span></div>
      <div class="row"><span>EDAMAME MIT SALZ/CHILI</span><span class="price">4,50€</span></div>
      <div>SEIDENTOFU in hausgemachter</div>
      <div class="row"><span>Sauce mit Mandeln</span><span class="price">5,50€</span></div>
    </div>

    <div class="section condensed" style="left:251px; top:128px;">
      <div class="section__head">SUSHIKLEINE GERICHTE</div>
      <div class="row"><span>URAMAKI mit Tempuragemüse</span><span class="price">8,90€</span></div>
      <div class="row"><span>GEMÜSE TEMPURA</span><span class="price">8,00€</span></div>
      <div class="row"><span>FUTOMAKI wechselndes Gemüse</span><span class="price">8,00€</span></div>
      <div class="row"><span>Crispy TOFUSTICKS mit Mayo</span><span class="price">8,00€</span></div>
      <div class="row"><span>URAMAKI mit Austernpilze</span><span class="price">7,50€</span></div>
      <div class="row"><span>KÜRBISKROKETTEN mit TANGASHU</span><span class="price">7,90€</span></div>
      <div class="row"><span>HOSOMAKI Gurke Avocado</span><span class="price">5,50€</span></div>
      <div class="row"><span>SUSHI "THUNA" CAKE</span><span class="price">6,90€</span></div>
      <div class="row"><span>HOSOMAKI Gurke Shiitake</span><span class="price">5,50€</span></div>
      <div class="row"><span>SUSHI CAKE CLASSIC</span><span class="price">6,00€</span></div>
      <div class="row"><span>TOMATEN NIGIRI</span><span class="price">4,50€</span></div>
      <div class="row"><span>AUBERGINE DENGAKU</span><span class="price">5,50€</span></div>
    </div>

    <div class="section spaced" style="left:374px; top:61px;">
      <div class="section__head">HAUPTSPEISEN</div>
      <div>Herrlich cremiges KATSU CURRY</div>
      <div>mit knusprigen Auberginensticks,</div>
      <div class="row"><span>Reis &amp; Pickles!</span><span class="price">7,90€</span></div>
      <div>RAMEN SUPPE mit Nudeln,Gemüse</div>
      <div class="row"><span>&amp; Tofu</span><span class="price">14,90€</span></div>
      <div class="row"><span>CHIRASHI SUSHI BOWL</span><span class="price">13,90€</span></div>
      <div>SOMMERSALATE mit</div>
      <div>Sesamdressing&amp; crispy</div>
      <div class="row"><span>Tofusticksmit Mayo</span><span class="price">12,50€</span></div>
    </div>

    <div class="section condensed dessert" style="left:374px; top:181px;">
      <div class="section__head">DESSERT</div>
      <div class="row"><span>CHEESECAKEmit Beeren</span><span class="price">6,50€</span></div>
      <div class="row"><span>PANA COTTA mit Beeren</span><span class="price">5,90€</span></div>
      <div class="row"><span>SORBETdes Tages</span><span class="price">5,50€</span></div>
      <div class="row"><span>SORBET des Tages mit Schuss</span><span class="price">6,90€</span></div>
    </div>

    <div class="vegan">All vegan</div>
    <div class="allergy">Bitte teilen Sie dem Service unbedingt Allergien mit und fragen Sie nach der Allergiker-Menükarte</div>
  </div>
</section>

</body>
</html>
```